R&K Security Services PTY. LTD.

Ive just had my logo made and I'm looking for some simple but strong designs for my business cards the company is a security company.

Please use dark colors.

Regards,

Dale Prentiss

Reason: Need more time for discussion with other directors

Industry/Entity Type

Security

Font styles to use
Sans Serif
Decorative

```html
<!DOCTYPE html>
<html lang="en">
<head>
<meta charset="utf-8">
<title>R&amp;K Security Services – Business Card</title>
<link href="https://fonts.googleapis.com/css2?family=Open+Sans:wght@400;600;700&display=swap" rel="stylesheet">
<style>
  :root {
    --backdrop: #a6a6a6;
    --card: #ffffff;
    --ink: #2b2b2b;
    --ink-soft: #555555;
    --tab-light: #d8d8d8;
    --tab-dark: #5a5a5a;
  }
  * { box-sizing: border-box; margin: 0; padding: 0; }
  html, body {
    width: 1200px; height: 894px; overflow: hidden;
    background: var(--backdrop);
    font-family: "Open Sans", Arial, sans-serif;
    color: var(--ink);
  }
  .stage { position: relative; width: 1200px; height: 894px; }
  .card {
    position: absolute; top: 293px;
    width: 540px; height: 308px;
    background: var(--card);
    box-shadow: 0 6px 18px rgba(0,0,0,.25);
    overflow: hidden;
  }
  .card--front { left: 40px; }
  .card--back { left: 620px; }

  .brand {
    position: absolute;
    font-weight: 700; color: var(--ink);
    letter-spacing: 1px;
  }
  .card--front .brand { left: 190px; top: 48px; font-size: 40px; }
  .card--back .brand { left: 0; right: 0; top: 92px; text-align: center; font-size: 44px; }

  .edge-tab {
    position: absolute; width: 26px; height: 34px;
    background: linear-gradient(90deg, var(--tab-dark), var(--tab-light) 55%, var(--tab-dark));
  }
  .card--front .edge-tab { left: 0; top: 126px; }
  .card--back .edge-tab { right: 0; top: 214px; }

  .holder { position: absolute; left: 40px; top: 124px; }
  .holder__name { font-size: 26px; font-weight: 700; letter-spacing: .5px; line-height: 1; }
  .holder__role { font-size: 13px; font-weight: 400; letter-spacing: 6px; color: var(--ink-soft); margin-top: 4px; }

  .contact {
    position: absolute; right: 34px; bottom: 28px;
    list-style: none; font-size: 12px; font-weight: 600; line-height: 1.25;
  }
  .contact li { display: flex; align-items: flex-start; gap: 10px; margin-top: 7px; }
  .contact svg { width: 14px; height: 14px; flex: none; fill: var(--ink); }

  .social {
    position: absolute; left: 50px; right: 50px; bottom: 52px;
    display: flex; justify-content: space-between;
    list-style: none; font-size: 13px; color: var(--ink-soft);
  }
  .social li { display: flex; align-items: center; gap: 8px; }
  .social__mark { width: 14px; height: 14px; background: var(--ink); }
</style>
</head>
<body>
<main class="stage">

  <section class="card card--front" aria-label="Business card front">
    <div class="brand">R&amp;K</div>
    <div class="edge-tab"></div>
    <div class="holder">
      <p class="holder__name">OWEN HARTLEY</p>
      <p class="holder__role">GENERAL MANAGER</p>
    </div>
    <ul class="contact">
      <li>
        <svg viewBox="0 0 16 16"><path d="M8 1 0 8h2v7h4v-5h4v5h4V8h2z"/></svg>
        <span>041.12th floor.Plaza<br>Kestrel Road NTH</span>
      </li>
      <li>
        <svg viewBox="0 0 16 16"><path d="M8 0a8 8 0 1 0 0 16A8 8 0 0 0 8 0zm0 1.5c.9 0 2 1.9 2.3 5.5H5.7C6 3.4 7.1 1.5 8 1.5zM1.6 7h2.6c.1-2 .5-3.7 1.1-4.8A6.5 6.5 0 0 0 1.6 7zm0 2a6.5 6.5 0 0 0 3.7 4.8C4.7 12.7 4.3 11 4.2 9zm4.1 0h4.6c-.3 3.6-1.4 5.5-2.3 5.5S6 12.6 5.7 9zm6.1 0h2.6a6.5 6.5 0 0 1-3.7 4.8c.6-1.1 1-2.8 1.1-4.8zm2.6-2h-2.6c-.1-2-.5-3.7-1.1-4.8A6.5 6.5 0 0 1 14.4 7z"/></svg>
        <span>www.yourwebsite.com</span>
      </li>
      <li>
        <svg viewBox="0 0 16 16"><path d="M0 3h16v1L8 9 0 4zm0 3 8 5 8-5v7H0z"/></svg>
        <span>yourname@email.com</span>
      </li>
      <li>
        <svg viewBox="0 0 16 16"><path d="M4 1 1.5 2.5C1 6 5 13 10.5 15L13 13l-2.5-3-2 1C7 10 6 8.5 5.5 6.5l2-1.5z"/></svg>
        <span>012 345 6789</span>
      </li>
    </ul>
  </section>

  <section class="card card--back" aria-label="Business card back">
    <div class="brand">R&amp;K</div>
    <div class="edge-tab"></div>
    <ul class="social">
      <li><span class="social__mark"></span>yourname</li>
      <li><span class="social__mark"></span>@yourname</li>
      <li><span class="social__mark"></span>yourname</li>
    </ul>
  </section>

</main>
</body>
</html>
```